Modern Spot UV Business Card design

We are a relatively new real estate agency. We need a business card that reflects the professionalism and prestige of our company but is also modern and fresh, based around our logo.
We would love to utilise spot UV.
Happy to let the designers use their imagination and see what they come up with (we're not very creative, so have no ideas for you, sorry) :-)
We'd like one for each staff member, but I've just provided one staff members photo here to avoid confusion.

Target Market(s)

Families

Industry/Entity Type

Real Estate Agent

Contact Information for Business Card

Colin Varga - Director & Principal
Mobile: 0491 527 806
Email: colin.varga@vbrokers.example.com.au
Phone: (08) 7364 9150
Fax: (08) 7364 9182
www.vargabrokersrealestate.example.com.au

Font styles to use
Other font styles liked:
• Kabel Dm BT

Requirements
Must have
• Contact details, logo, photo, spot UV
Nice to have
• Modern interesting features that will make people comment. Nothing too feminine nor too masculine.
Should not have
• No houses! Nothing typical of a real estate agent.

```html
<!DOCTYPE html>
<html lang="en">
<head>
<meta charset="UTF-8">
<title>VargaBrokers – Business Card</title>
<link rel="stylesheet" href="https://fonts.googleapis.com/css2?family=Poppins:wght@500;600;700&display=swap">
<style>
  :root {
    --backdrop: #b3b2b3;
    --card: #ffffff;
    --ink: #1c1c1c;
    --ink-soft: #3d3d3d;
    --blue: #1e8fd6;
    --orange: #f7931e;
    --photo-light: #eef0f2;
    --photo-dark: #8a8f96;
  }
  * { box-sizing: border-box; margin: 0; padding: 0; }
  html, body {
    width: 1200px; height: 900px; overflow: hidden;
    background: var(--backdrop);
    font-family: "Poppins", sans-serif;
    color: var(--ink);
  }
  .card {
    position: absolute;
    width: 680px; height: 389px;
    background: var(--card);
    box-shadow: 0 6px 18px rgba(0,0,0,.25);
  }
  .card--front { left: 100px; top: 40px; }
  .card--back  { left: 420px; top: 470px; }

  /* Brand name */
  .brand {
    position: absolute;
    display: flex; align-items: center; gap: 10px;
    font-weight: 700; font-size: 40px; line-height: 1; letter-spacing: -.5px;
    color: var(--ink);
  }
  .brand__dot {
    width: 18px; height: 18px; border-radius: 50%;
    background: var(--orange); flex: none;
  }
  .card--front .brand { left: 40px; top: 70px; }
  .card--back .brand { left: 198px; top: 170px; }

  /* Portrait */
  .portrait {
    position: absolute; left: 470px; top: 48px;
    width: 174px; height: 174px; border-radius: 50%;
    border: 2px solid var(--blue);
    padding: 4px; background: var(--card);
  }
  .portrait__fill {
    width: 100%; height: 100%; border-radius: 50%;
    background: linear-gradient(180deg, var(--photo-light) 0%, var(--photo-light) 45%, var(--photo-dark) 100%);
  }

  /* Name ribbons */
  .ribbon {
    position: absolute; height: 28px;
    display: flex; align-items: center; justify-content: center;
    font-weight: 600; font-size: 14px; color: var(--ink);
    clip-path: polygon(12px 0, 100% 0, calc(100% - 12px) 100%, 0 100%);
  }
  .ribbon--name {
    left: 450px; top: 230px; width: 210px;
    background: var(--orange); text-transform: uppercase; letter-spacing: .3px;
  }
  .ribbon--title {
    left: 410px; top: 264px; width: 215px;
    background: var(--blue); font-weight: 500;
  }

  /* Contact list */
  .contacts {
    position: absolute; left: 40px; top: 218px;
    list-style: none;
  }
  .contacts__item {
    display: flex; align-items: center; gap: 14px;
    font-weight: 500; font-size: 16.5px; line-height: 27px; color: var(--ink);
  }
  .contacts__icon { width: 16px; height: 16px; flex: none; fill: var(--blue); }

  /* Back side rules */
  .rule { position: absolute; height: 1.5px; background: var(--blue); }
  .rule--left  { left: 0; top: 142px; width: 180px; }
  .rule--right { right: 0; top: 242px; width: 180px; }
</style>
</head>
<body>

<section class="card card--front" aria-label="Business card front">
  <div class="brand"><span class="brand__dot"></span>VargaBrokers</div>

  <div class="portrait">
    <div class="portrait__fill" role="img" aria-label="Portrait photo of Colin Varga in a suit"></div>
  </div>

  <div class="ribbon ribbon--name">Colin Varga</div>
  <div class="ribbon ribbon--title">Director &amp; Principal</div>

  <ul class="contacts">
    <li class="contacts__item">
      <svg class="contacts__icon" viewBox="0 0 16 16" aria-label="Mobile"><path d="M4 1h8a1 1 0 0 1 1 1v12a1 1 0 0 1-1 1H4a1 1 0 0 1-1-1V2a1 1 0 0 1 1-1zm1 2v9h6V3z"/></svg>
      0491 527 806
    </li>
    <li class="contacts__item">
      <svg class="contacts__icon" viewBox="0 0 16 16" aria-label="Phone"><path d="M3.5 1l2.5 3-1.5 2c1 2 3 4 5 5l2-1.5 3 2.5-1.5 2.5C7 14.5 1.5 9 1 3z"/></svg>
      (08) 7364 9150
    </li>
    <li class="contacts__item">
      <svg class="contacts__icon" viewBox="0 0 16 16" aria-label="Fax"><path d="M4 1h8v4H4zM1 6h14v6h-2v3H3v-3H1zm4 4v3h6v-3z"/></svg>
      (08) 7364 9182
    </li>
    <li class="contacts__item">
      <svg class="contacts__icon" viewBox="0 0 16 16" aria-label="Email"><path d="M1 4h14v9H1zm1.5 1.2L8 9.2l5.5-4z"/></svg>
      colin.varga@vbrokers.example.com.au
    </li>
    <li class="contacts__item">
      <svg class="contacts__icon" viewBox="0 0 16 16" aria-label="Website"><circle cx="8" cy="8" r="7"/><path d="M1 8h14M8 1c3 3 3 11 0 14M8 1c-3 3-3 11 0 14" stroke="#fff" stroke-width="1" fill="none"/></svg>
      www.vargabrokersrealestate.example.com.au
    </li>
  </ul>
</section>

<section class="card card--back" aria-label="Business card back">
  <div class="rule rule--left"></div>
  <div class="brand"><span class="brand__dot"></span>VargaBrokers</div>
  <div class="rule rule--right"></div>
</section>

</body>
</html>
```